I need a Facebook, Instagram post, for Outdoor Training
I need my logo,
Business name : Valmora Soccer Academy
Boys and girls Outdoor Soccer training
Passing, Kicking Shooting, Dribbling, Ball Control
Field: Brookvale Turf #5(1746 Hollowmere Lane Dunstead, MD 20419)
Time: 5:30pm-6:30pm 5-8 years old
6;30pm-7:30pm 9-12 years old
7:30pm-8:30pm 13-18 years old
Registration $210 ( Includes 1st month, registration, practice uniform)

Register online:
www.valmoraacademy.example
Phone:(240)555-0187

Target Market(s)

YOUTH KIDS

Colors
0054AA
0677BA
7BADD7
CADEEF
E8F1F8

Requirements
Must have
• blue , or black and white

```html
<!DOCTYPE html>
<html lang="en">
<head>
<meta charset="utf-8">
<title>Valmora Soccer Academy – Outdoor Training</title>
<link href="https://fonts.googleapis.com/css2?family=Saira:wght@600;700&family=Saira+Condensed:wght@500;600;700&family=Catamaran:wght@500;600&display=swap" rel="stylesheet">
<style>
  :root{
    --ink:#0b0b0c;
    --blue:#0054aa;
    --blue-mid:#0677ba;
    --blue-band:#0a5aa0;
    --sky:#7badd7;
    --pale:#cadeef;
    --white:#ffffff;
    --tick:#1fa3e0;
  }
  *{margin:0;padding:0;box-sizing:border-box}
  html,body{width:1200px;height:1200px;overflow:hidden;background:var(--ink)}
  .post{position:relative;width:1200px;height:1200px;background:var(--ink);overflow:hidden;color:var(--white);font-family:"Catamaran",sans-serif}
  .backdrop{position:absolute;inset:0}
  .brand{position:absolute;left:70px;top:150px;display:flex;align-items:center;gap:14px}
  .brand-dot{width:22px;height:22px;border-radius:50%;background:var(--blue)}
  .brand-name{font-family:"Saira",sans-serif;font-weight:700;font-size:26px;line-height:1.1;color:var(--white);text-transform:uppercase}
  .title{position:absolute;left:60px;font-family:"Saira",sans-serif;font-weight:700;text-transform:uppercase;line-height:1;letter-spacing:1px}
  .title-main{top:488px;font-size:126px;color:var(--white)}
  .title-sub{top:612px;font-size:92px;color:var(--blue-mid);letter-spacing:2px}
  .banner{position:absolute;left:0;top:712px;width:940px;height:66px}
  .banner-text{position:absolute;left:62px;top:718px;font-family:"Saira",sans-serif;font-weight:700;font-size:37px;letter-spacing:1px;line-height:54px;text-transform:uppercase}
  .skills{position:absolute;left:62px;top:788px;font-size:31px;font-weight:500}
  .label{position:absolute;background:var(--blue);color:var(--white);font-weight:500;display:flex;align-items:center;justify-content:center;border-radius:2px}
  .field-label{left:65px;top:884px;width:97px;height:38px;font-size:23px}
  .rule{position:absolute;height:1px;background:#d8d8d8}
  .rule-top{left:173px;top:889px;width:690px}
  .rule-bottom{left:63px;top:938px;width:800px}
  .field-text{position:absolute;left:174px;top:898px;font-size:20px;font-weight:500;line-height:28px}
  .session{position:absolute;top:962px;width:240px}
  .session svg{display:block;width:26px;height:26px}
  .session-time{font-family:"Saira Condensed",sans-serif;font-weight:600;font-size:32px;line-height:1;margin-top:14px}
  .session-age{font-size:26px;font-weight:500;line-height:1;margin-top:10px}
  .divider{position:absolute;top:965px;width:6px;height:98px;border-left:1px solid #cfcfcf;border-right:1px solid #cfcfcf}
  .price{position:absolute;left:885px;top:886px;width:236px;height:172px;background:var(--blue);border-radius:12px;text-align:center}
  .price-label{font-weight:600;font-size:19px;margin-top:12px;line-height:1}
  .price-amount{font-family:"Saira Condensed",sans-serif;font-weight:700;font-size:100px;line-height:0.9;margin-top:4px;position:relative;display:inline-block;padding-left:18px}
  .price-amount span{position:absolute;left:-14px;top:4px;font-size:46px}
  .price-note{font-size:14.5px;font-weight:500;line-height:1.3;margin-top:6px}
  .register-label{left:63px;top:1125px;width:215px;height:38px;font-size:25px}
  .register-url{position:absolute;left:296px;top:1126px;font-size:25px;font-weight:500;line-height:34px}
  .call{position:absolute;right:79px;top:1112px;font-family:"Saira Condensed",sans-serif;font-weight:700;font-size:52px;line-height:1;white-space:nowrap}
  .call-cue{color:var(--blue-mid);margin-right:8px}
</style>
</head>
<body>
<main class="post">
  <svg class="backdrop" width="1200" height="1200" viewBox="0 0 1200 1200">
    <defs>
      <linearGradient id="fieldPhoto" x1="0" y1="0" x2="0.6" y2="1">
        <stop offset="0" stop-color="#2f6a4a"/>
        <stop offset="0.35" stop-color="#7a9a5a"/>
        <stop offset="0.7" stop-color="#a8c64a"/>
        <stop offset="1" stop-color="#8fb83e"/>
      </linearGradient>
    </defs>
    <polygon class="accent-band" fill="var(--blue-band)" points="0,79 280,260 997,666 1200,516 1200,780 110,288 0,386"/>
    <polygon role="img" aria-label="Photo of children in colourful kits running with soccer balls on a grass field" fill="url(#fieldPhoto)" points="0,0 1200,0 1200,516 997,666 280,260 0,79"/>
  </svg>

  <div class="brand">
    <div class="brand-dot"></div>
    <div class="brand-name">Valmora<br>Soccer Academy</div>
  </div>

  <h1 class="title title-main">Valmora</h1>
  <h2 class="title title-sub">Soccer Academy</h2>

  <svg class="banner" width="940" height="66" viewBox="0 0 940 66">
    <polygon points="0,3 908,3 933,63 0,63" fill="var(--blue-band)" stroke="var(--white)" stroke-width="4"/>
  </svg>
  <p class="banner-text">Boys and Girls Outdoor Soccer Training</p>

  <p class="skills">Passing, Kicking Shooting, Dribbling, Ball Control</p>

  <div class="label field-label">Field:</div>
  <div class="rule rule-top"></div>
  <p class="field-text">Brookvale Turf #5(1746 Hollowmere Lane Dunstead, MD 20419)</p>
  <div class="rule rule-bottom"></div>

  <div class="session" style="left:65px">
    <svg viewBox="0 0 26 26"><circle cx="13" cy="13" r="13" fill="var(--tick)"/><path d="M7 13.5l4 4 8-8" fill="none" stroke="var(--ink)" stroke-width="2.6" stroke-linecap="round" stroke-linejoin="round"/></svg>
    <p class="session-time">5:30PM - 6:30PM</p>
    <p class="session-age">5-8 years old</p>
  </div>
  <div class="divider" style="left:306px"></div>
  <div class="session" style="left:362px">
    <svg viewBox="0 0 26 26"><circle cx="13" cy="13" r="13" fill="var(--tick)"/><path d="M7 13.5l4 4 8-8" fill="none" stroke="var(--ink)" stroke-width="2.6" stroke-linecap="round" stroke-linejoin="round"/></svg>
    <p class="session-time">6:30PM - 7:30PM</p>
    <p class="session-age">9-12 years old</p>
  </div>
  <div class="divider" style="left:603px"></div>
  <div class="session" style="left:659px">
    <svg viewBox="0 0 26 26"><circle cx="13" cy="13" r="13" fill="var(--tick)"/><path d="M7 13.5l4 4 8-8" fill="none" stroke="var(--ink)" stroke-width="2.6" stroke-linecap="round" stroke-linejoin="round"/></svg>
    <p class="session-time">7:30PM - 8:30PM</p>
    <p class="session-age">13-18 years old</p>
  </div>

  <div class="price">
    <p class="price-label">REGISTRATION</p>
    <p class="price-amount"><span>$</span>210</p>
    <p class="price-note">( Includes 1st month,<br>registration, practice uniform)</p>
  </div>

  <div class="label register-label">Register online:</div>
  <p class="register-url">www.valmoraacademy.example</p>
  <p class="call"><span class="call-cue">CALL NOW</span>(240) 555-0187</p>
</main>
</body>
</html>
```